Naturopath Practitioner Card Design

I am a naturopath needing a design for a business card mainly to show that I am a naturopath and have some contact details to give to prospective clients. I am open minded about the design and what is on the second side of the card whether it just be some artwork or space for details, appointment times etc. Naturopathy is the practice of natural medicine that uses a holistic approach and incorporates herbal and nutritional medicine.

Contact Information for Business Card

Tom Waverly NaturopathBHSc (Naturopathy) Member NHPG 0491 582 736 tom.waverly@mailbox-example.net www.tomwaverlynaturopathy.example.au

Requirements
Nice to have
• Would prefer some kind of original pattern/art work/logo rather than an image, not fussed if its very simple/basic
• I am open to any colour but think I would prefer a more earthy sandy clay etc type style than the greens that are commonly associated with naturopathy.
Should not have
• Don't really want to have generic stock images on it

```html
<!DOCTYPE html>
<html lang="en">
<head>
<meta charset="utf-8">
<title>Tom Waverly Naturopath – Business Card</title>
<link rel="stylesheet" href="https://fonts.googleapis.com/css2?family=Questrial&display=swap">
<style>
  :root {
    --stage: #1c1c1c;
    --paper: #ffffff;
    --lime: #a3cc39;
    --lime-light: #c4e07a;
    --leaf: #7fa83a;
    --forest: #4f7a2a;
    --ink: #2a2a2a;
    --rule: #8db43f;
  }
  * { box-sizing: border-box; margin: 0; padding: 0; }
  html, body {
    width: 1200px; height: 912px; overflow: hidden;
    background: var(--stage);
    font-family: "Questrial", "Century Gothic", sans-serif;
  }
  .card {
    position: absolute; left: 300px;
    width: 600px; height: 350px;
    background: var(--paper);
    border-radius: 18px; overflow: hidden;
  }
  .card--appointment { top: 80px; }
  .card--front { top: 482px; }

  /* Appointment side */
  .appt-title {
    position: absolute; top: 22px; left: 300px;
    color: var(--leaf); font-size: 22px; font-weight: 400; letter-spacing: 0.5px;
  }
  .appt-row {
    position: absolute; left: 34px; right: 34px;
    display: flex; align-items: flex-end; gap: 6px;
    color: var(--leaf); font-size: 14px;
  }
  .appt-row .fill { flex: 1; border-bottom: 1px solid var(--rule); height: 14px; }
  .appt-row .fill--date { flex: 1.1; }
  .appt-row .ampm { width: 56px; text-align: right; }
  .days {
    position: absolute; top: 244px; left: 34px; right: 34px;
    display: flex; justify-content: space-between;
    color: var(--leaf); font-size: 18px;
  }
  .day { display: flex; align-items: center; gap: 4px; }
  .day .box { width: 18px; height: 18px; border: 2px solid var(--leaf); }
  .notice-band {
    position: absolute; left: 0; right: 0; bottom: 0; height: 70px;
    background: linear-gradient(90deg, var(--leaf), var(--lime) 60%, var(--leaf));
    color: var(--paper); text-align: center;
    font-size: 14px; letter-spacing: 0.5px; line-height: 1.5;
    padding-top: 14px;
  }

  /* Front side */
  .practitioner { position: absolute; top: 30px; left: 30px; }
  .practitioner__name { color: var(--lime); font-size: 30px; font-weight: 400; letter-spacing: 0.5px; }
  .practitioner__degree { color: var(--ink); font-size: 16px; margin-top: 2px; }
  .wave { position: absolute; inset: 0; }
  .contact {
    position: absolute; right: 26px; top: 196px;
    color: var(--ink); font-size: 15px; text-align: right; line-height: 1.7;
  }
  .contact__item { display: flex; justify-content: flex-end; align-items: center; gap: 8px; }
  .contact__item svg { flex: none; }
</style>
</head>
<body>

<section class="card card--appointment">
  <h2 class="appt-title">Appointment</h2>
  <div class="appt-row" style="top:60px"><span>Name:</span><span class="fill"></span></div>
  <div class="appt-row" style="top:100px"><span>Date:</span><span class="fill fill--date"></span><span>Time :</span><span class="fill"></span><span class="ampm">am / pm</span></div>
  <div class="appt-row" style="top:136px"><span>Date:</span><span class="fill fill--date"></span><span>Time :</span><span class="fill"></span><span class="ampm">am / pm</span></div>
  <div class="appt-row" style="top:172px"><span>Date:</span><span class="fill fill--date"></span><span>Time :</span><span class="fill"></span><span class="ampm">am / pm</span></div>
  <div class="appt-row" style="top:208px"><span>Date:</span><span class="fill fill--date"></span><span>Time :</span><span class="fill"></span><span class="ampm">am / pm</span></div>
  <div class="days">
    <span class="day">MON<span class="box"></span></span>
    <span class="day">TUE<span class="box"></span></span>
    <span class="day">WED<span class="box"></span></span>
    <span class="day">THU<span class="box"></span></span>
    <span class="day">FRI<span class="box"></span></span>
    <span class="day">SAT<span class="box"></span></span>
  </div>
  <div class="notice-band">PLEASE NOTIFY US 24HRS IN ADVANCE IF YOU NEED TO CANCEL<br>YOUR APPOINTENT</div>
</section>

<section class="card card--front">
  <svg class="wave" viewBox="0 0 600 350" width="600" height="350" aria-hidden="true">
    <defs>
      <linearGradient id="waveFill" x1="0" y1="0" x2="1" y2="0">
        <stop offset="0" stop-color="#a3cc39"/>
        <stop offset="0.5" stop-color="#c4e07a"/>
        <stop offset="1" stop-color="#a3cc39"/>
      </linearGradient>
    </defs>
    <path d="M0,160 C100,150 170,200 240,258 S450,328 600,330 L600,350 L0,350 Z" fill="url(#waveFill)"/>
    <path d="M0,150 C100,140 170,190 240,250 S450,320 600,322" fill="none" stroke="#4f7a2a" stroke-width="6"/>
    <path d="M0,156 C100,146 170,196 240,255 S450,325 600,327" fill="none" stroke="#ffffff" stroke-width="2"/>
  </svg>
  <div class="practitioner">
    <h1 class="practitioner__name">Tom Waverly Naturopath</h1>
    <p class="practitioner__degree">BHSc (Naturopathy)</p>
  </div>
  <div class="contact">
    <p class="contact__item">tom.waverly@mailbox-example.net
      <svg width="18" height="13" viewBox="0 0 18 13" aria-hidden="true"><rect x="0.5" y="0.5" width="17" height="12" fill="#7fa83a" stroke="#4f7a2a"/><path d="M1,1 L9,7 L17,1" fill="none" stroke="#fff" stroke-width="1.2"/></svg>
    </p>
    <p class="contact__item">www.tomwaverlynaturopathy.example.au
      <svg width="18" height="18" viewBox="0 0 18 18" aria-hidden="true"><circle cx="9" cy="9" r="8" fill="#7fa83a"/><g fill="none" stroke="#fff" stroke-width="1"><ellipse cx="9" cy="9" rx="3.5" ry="8"/><path d="M1,9 H17 M2.5,5 H15.5 M2.5,13 H15.5"/></g></svg>
    </p>
  </div>
</section>

</body>
</html>
```